Residential exterior painting postcard

Looking to have a postcard made for exterior residential painting. Our company page is Mesquitewallboard.com. We want something that catches our customers eye and makes them make a phone call. Include an offer of some sort on the card in form of free esitmates or discounts on materials etc. Must be an acceptable format for NPDS mailing. Color on both sides. Also too look high end as we are going for middle and upper class customers. Should also show our logo but make it very obvious that we are also a painting contractor. License number must also be visible and include that we are licensed bonded and insured.
License number 718296

Target Market(s)

Scottsdale, AZ, Paradise Valley, AZ Cave creek, AZ
Middle to upper class homeowners for exterior paint jobs

Industry/Entity Type

Construction Company

Font styles to use
Other font styles liked:
• Eras Medium ITC

Colors
0293ce
0455a3
3176b5
ffffff
000000
9d9d9d
cadf82
9bcb3b

Requirements
Must have
• License number, logo, contact number, website, pictures, calls to action
Nice to have
• Specific font info for our logo:
• Eras Medium ITC:
• All caps
• 23pt
• 27.6 leading
• 250% vertical scale
• -35 baseline shift
• Auto kerning
• 100% horizontal scale
• C: 97.69%
• M: 75.43%
• Y: 4.46%
• K: 0.03%

```html
<!DOCTYPE html>
<html lang="en">
<head>
<meta charset="utf-8">
<title>Mesquite Wallboard – Residential Painting Postcard</title>
<link href="https://fonts.googleapis.com/css2?family=Cinzel:wght@400;700&family=Oswald:wght@400;500;600&display=swap" rel="stylesheet">
<style>
  :root {
    --sky-blue: #0293ce;
    --deep-blue: #0455a3;
    --mid-blue: #3176b5;
    --white: #ffffff;
    --black: #000000;
    --grey: #9d9d9d;
    --light-green: #cadf82;
    --green: #9bcb3b;
    --backdrop: #2e2e30;
    --panel: #f1f2f3;
  }
  * { margin: 0; padding: 0; box-sizing: border-box; }
  html, body { width: 1000px; height: 1200px; overflow: hidden; background: var(--backdrop); }
  .canvas { position: relative; width: 1000px; height: 1200px; }

  .card { position: absolute; left: 70px; width: 860px; background: var(--white); overflow: hidden; }
  .card-front { top: 30px; height: 552px; background: linear-gradient(180deg, #ffffff 0%, #eef0f2 100%); }
  .card-back { top: 615px; height: 553px; }
  .card svg.art { position: absolute; inset: 0; }

  .brand { position: absolute; display: flex; align-items: center; gap: 10px; }
  .brand-dot { width: 14px; height: 14px; border-radius: 50%; background: var(--deep-blue); }
  .brand-name { font-family: "Oswald", sans-serif; font-weight: 400; font-size: 30px; color: var(--deep-blue); letter-spacing: 0.5px; text-transform: uppercase; }
  .card-front .brand { left: 30px; top: 26px; }
  .card-back .brand { left: 485px; top: 50px; }
  .card-back .brand-name { font-size: 26px; }

  .heritage { position: absolute; left: 20px; top: 138px; width: 405px; height: 90px; background: var(--green); padding: 5px; }
  .heritage-inner { width: 100%; height: 100%; border: 1px dashed rgba(255,255,255,0.8); display: flex; flex-direction: column; justify-content: center; padding-left: 16px; }
  .heritage-line { font-family: "Cinzel", serif; font-weight: 700; color: var(--white); font-size: 30px; line-height: 40px; }

  .expert-label { position: absolute; left: 44px; top: 268px; font-family: "Cinzel", serif; font-weight: 700; font-size: 22px; color: var(--white); letter-spacing: 0.5px; }
  .service-title { position: absolute; left: 42px; top: 316px; font-family: "Cinzel", serif; font-weight: 700; font-size: 28px; line-height: 36px; color: var(--black); letter-spacing: 0.5px; }
  .service-more { position: absolute; left: 42px; top: 390px; font-family: "Cinzel", serif; font-weight: 700; font-size: 11px; color: var(--black); }

  .offer { position: absolute; left: 42px; top: 420px; font-family: "Oswald", sans-serif; font-weight: 600; font-size: 21px; line-height: 27px; color: #1d2a12; text-transform: uppercase; }
  .offer-highlight { color: var(--white); }
  .call-icon { position: absolute; left: 437px; top: 424px; width: 44px; height: 44px; }
  .phone-number { position: absolute; left: 505px; top: 424px; font-family: "Cinzel", serif; font-weight: 700; font-size: 30px; color: var(--white); }
  .license-line { position: absolute; left: 44px; top: 484px; font-family: "Oswald", sans-serif; font-weight: 400; font-size: 20px; color: var(--white); text-transform: uppercase; }
  .web-line { position: absolute; left: 44px; top: 520px; display: flex; align-items: center; gap: 14px; font-family: "Cinzel", serif; font-weight: 700; font-size: 22px; color: var(--white); }

  .services-heading { position: absolute; left: 22px; top: 12px; font-family: "Cinzel", serif; font-weight: 700; font-size: 14.5px; color: var(--white); }
  .services-list { position: absolute; left: 22px; top: 42px; list-style: none; }
  .services-list li { font-family: "Cinzel", serif; font-size: 11.6px; line-height: 16.4px; color: #222; display: flex; align-items: center; gap: 6px; }
  .tick { width: 11px; height: 10px; flex: none; }

  .contact { position: absolute; left: 38px; top: 343px; font-family: "Cinzel", serif; color: #222; }
  .contact-title { font-weight: 700; font-size: 20px; color: var(--deep-blue); margin-bottom: 6px; }
  .contact-line { font-size: 17px; line-height: 25px; }

  .stamp-box { position: absolute; left: 745px; top: 30px; width: 87px; height: 90px; border: 1px solid #444; }
</style>
</head>
<body>
<main class="canvas">

  <!-- Front of postcard -->
  <section class="card card-front">
    <svg class="art" width="860" height="552" viewBox="0 0 860 552" aria-hidden="false">
      <defs>
        <linearGradient id="homePhoto" x1="0" y1="0" x2="0" y2="1">
          <stop offset="0" stop-color="#3f86d6"/>
          <stop offset="0.28" stop-color="#8fb6d8"/>
          <stop offset="0.4" stop-color="#b9a58b"/>
          <stop offset="0.7" stop-color="#9c8a74"/>
          <stop offset="0.88" stop-color="#5f7d3c"/>
          <stop offset="1" stop-color="#c9bfae"/>
        </linearGradient>
      </defs>
      <path role="img" aria-label="Photo of a large stone two-storey family home with gables, arched windows and green trees under a blue sky"
            d="M385,0 L860,0 L860,552 L680,552 C620,430 520,330 470,200 C440,120 405,60 385,0 Z" fill="url(#homePhoto)"/>
      <path d="M330,0 L395,0 C420,80 460,170 500,260 C560,390 640,470 690,552 L650,552 C590,460 500,360 450,250 C400,150 350,70 330,0 Z" fill="var(--sky-blue)"/>
      <path d="M372,0 L392,0 C418,80 458,170 498,260 C556,386 632,466 684,552 L672,552 C618,466 540,384 484,262 C440,170 398,80 372,0 Z" fill="var(--deep-blue)"/>
      <polygon points="0,265 470,265 455,305 0,305" fill="var(--sky-blue)"/>
      <polygon points="0,415 750,415 735,475 0,475" fill="var(--green)"/>
      <polygon points="0,480 690,480 672,518 0,518" fill="var(--sky-blue)"/>
      <polygon points="0,518 445,518 430,552 0,552" fill="var(--green)"/>
    </svg>

    <div class="brand"><span class="brand-dot"></span><span class="brand-name">Mesquite Wallboard</span></div>

    <div class="heritage">
      <div class="heritage-inner">
        <span class="heritage-line">A Family Tradition</span>
        <span class="heritage-line">Established in 1954</span>
      </div>
    </div>

    <p class="expert-label">WE ARE EXPERT IN</p>
    <h1 class="service-title">RESIDENTIAL EXTERIOR<br>PAINTING</h1>
    <p class="service-more">&amp; MANY MORE</p>

    <p class="offer">Call now and <span class="offer-highlight">get free esitmates</span><br>Discounts on materials etc</p>

    <svg class="call-icon" viewBox="0 0 44 44" aria-hidden="true">
      <circle cx="22" cy="22" r="20" fill="var(--deep-blue)" stroke="var(--white)" stroke-width="3"/>
      <path d="M16 12 c-2 1 -3 3 -2 6 c2 6 6 10 12 13 c3 1 5 0 6 -2 l-4 -4 c-1 0 -2 1 -3 1 c-3 -2 -5 -4 -6 -7 c0 -1 1 -2 1 -3 Z" fill="var(--white)"/>
    </svg>
    <p class="phone-number">480-555-0173</p>

    <p class="license-line">Licensed bonded and insured. License number 718296</p>

    <p class="web-line">
      <svg width="20" height="20" viewBox="0 0 20 20" aria-hidden="true">
        <g fill="none" stroke="var(--white)" stroke-width="1.5">
          <circle cx="10" cy="10" r="8.5"/><ellipse cx="10" cy="10" rx="3.8" ry="8.5"/>
          <line x1="1.5" y1="10" x2="18.5" y2="10"/><line x1="3" y1="5.5" x2="17" y2="5.5"/><line x1="3" y1="14.5" x2="17" y2="14.5"/>
        </g>
      </svg>
      Mesquitewallboard.com
    </p>
  </section>

  <!-- Back of postcard -->
  <section class="card card-back">
    <svg class="art" width="860" height="553" viewBox="0 0 860 553">
      <defs>
        <linearGradient id="panelFade" x1="0" y1="0" x2="0" y2="1">
          <stop offset="0" stop-color="#ffffff"/>
          <stop offset="0.65" stop-color="#f1f2f3"/>
          <stop offset="1" stop-color="#e6e6e2"/>
        </linearGradient>
        <linearGradient id="desertPhoto" x1="0" y1="0" x2="0" y2="1">
          <stop offset="0" stop-color="#e8ebee"/>
          <stop offset="0.6" stop-color="#d6d2c4"/>
          <stop offset="1" stop-color="#c4c9b6"/>
        </linearGradient>
        <linearGradient id="thumbA" x1="0" y1="0" x2="0" y2="1"><stop offset="0" stop-color="#8fb7d9"/><stop offset="1" stop-color="#7a6a55"/></linearGradient>
        <linearGradient id="thumbB" x1="0" y1="0" x2="0" y2="1"><stop offset="0" stop-color="#b88a58"/><stop offset="1" stop-color="#6d5a3e"/></linearGradient>
        <linearGradient id="thumbC" x1="0" y1="0" x2="0" y2="1"><stop offset="0" stop-color="#c9d3c6"/><stop offset="1" stop-color="#6f7f57"/></linearGradient>
        <linearGradient id="thumbD" x1="0" y1="0" x2="0" y2="1"><stop offset="0" stop-color="#8a5a34"/><stop offset="1" stop-color="#4b3020"/></linearGradient>
      </defs>
      <path d="M0,0 L405,0 C415,60 425,120 440,185 C410,290 370,380 325,475 L0,475 Z" fill="url(#panelFade)"/>
      <rect role="img" aria-label="Faded photo of a desert home with landscaping" x="0" y="330" width="400" height="145" fill="url(#desertPhoto)" opacity="0.85"/>
      <path d="M405,0 L432,0 C444,60 460,120 472,185 C442,290 402,380 352,475 L325,475 C370,380 410,290 440,185 C425,120 415,60 405,0 Z" fill="var(--sky-blue)"/>
      <path d="M418,0 L424,0 C436,60 452,120 462,185 C432,290 392,380 342,475 L336,475 C382,380 422,290 452,185 C438,120 428,60 418,0 Z" fill="var(--deep-blue)"/>
      <polygon points="0,9 410,9 414,33 0,33" fill="var(--green)"/>
      <g stroke="var(--green)" stroke-width="4">
        <circle role="img" aria-label="Photo of a painted home entrance with covered porch" cx="375" cy="76" r="36" fill="url(#thumbA)"/>
        <circle role="img" aria-label="Photo of a desert hillside home" cx="405" cy="155" r="36" fill="url(#thumbB)"/>
        <circle role="img" aria-label="Photo of a freshly painted home exterior" cx="366" cy="232" r="36" fill="url(#thumbC)"/>
        <circle role="img" aria-label="Photo of a refinished living room interior" cx="330" cy="313" r="36" fill="url(#thumbD)"/>
      </g>
    </svg>

    <h2 class="services-heading">Residential Painting Services Include:</h2>
    <ul class="services-list">
      <li><svg class="tick" viewBox="0 0 11 10"><path d="M1 5 L4 8 L10 1" fill="none" stroke="var(--sky-blue)" stroke-width="1.6"/></svg>Interior &amp; Exterior Painting</li>
      <li><svg class="tick" viewBox="0 0 11 10"><path d="M1 5 L4 8 L10 1" fill="none" stroke="var(--sky-blue)" stroke-width="1.6"/></svg>Wood staining packages</li>
      <li><svg class="tick" viewBox="0 0 11 10"><path d="M1 5 L4 8 L10 1" fill="none" stroke="var(--sky-blue)" stroke-width="1.6"/></svg>Drywall repair &amp; texture matching</li>
      <li><svg class="tick" viewBox="0 0 11 10"><path d="M1 5 L4 8 L10 1" fill="none" stroke="var(--sky-blue)" stroke-width="1.6"/></svg>Stucco repair</li>
      <li><svg class="tick" viewBox="0 0 11 10"><path d="M1 5 L4 8 L10 1" fill="none" stroke="var(--sky-blue)" stroke-width="1.6"/></svg>Venetian Plaster</li>
      <li><svg class="tick" viewBox="0 0 11 10"><path d="M1 5 L4 8 L10 1" fill="none" stroke="var(--sky-blue)" stroke-width="1.6"/></svg>Elastomeric Coatings</li>
      <li><svg class="tick" viewBox="0 0 11 10"><path d="M1 5 L4 8 L10 1" fill="none" stroke="var(--sky-blue)" stroke-width="1.6"/></svg>Epoxy Coatings</li>
      <li><svg class="tick" viewBox="0 0 11 10"><path d="M1 5 L4 8 L10 1" fill="none" stroke="var(--sky-blue)" stroke-width="1.6"/></svg>Environmentally friendly coatings</li>
      <li><svg class="tick" viewBox="0 0 11 10"><path d="M1 5 L4 8 L10 1" fill="none" stroke="var(--sky-blue)" stroke-width="1.6"/></svg>Electrostatic applications</li>
      <li><svg class="tick" viewBox="0 0 11 10"><path d="M1 5 L4 8 L10 1" fill="none" stroke="var(--sky-blue)" stroke-width="1.6"/></svg>Graffiti removal &amp; anti-graffiti coatings</li>
      <li><svg class="tick" viewBox="0 0 11 10"><path d="M1 5 L4 8 L10 1" fill="none" stroke="var(--sky-blue)" stroke-width="1.6"/></svg>Historical restorations</li>
      <li><svg class="tick" viewBox="0 0 11 10"><path d="M1 5 L4 8 L10 1" fill="none" stroke="var(--sky-blue)" stroke-width="1.6"/></svg>Maintenance painting programs</li>
      <li><svg class="tick" viewBox="0 0 11 10"><path d="M1 5 L4 8 L10 1" fill="none" stroke="var(--sky-blue)" stroke-width="1.6"/></svg>Roof coatings</li>
      <li><svg class="tick" viewBox="0 0 11 10"><path d="M1 5 L4 8 L10 1" fill="none" stroke="var(--sky-blue)" stroke-width="1.6"/></svg>Polyurethane &amp; UV Protective coatings</li>
      <li><svg class="tick" viewBox="0 0 11 10"><path d="M1 5 L4 8 L10 1" fill="none" stroke="var(--sky-blue)" stroke-width="1.6"/></svg>Pressure washing</li>
      <li><svg class="tick" viewBox="0 0 11 10"><path d="M1 5 L4 8 L10 1" fill="none" stroke="var(--sky-blue)" stroke-width="1.6"/></svg>Repaints</li>
      <li><svg class="tick" viewBox="0 0 11 10"><path d="M1 5 L4 8 L10 1" fill="none" stroke="var(--sky-blue)" stroke-width="1.6"/></svg>Cabinet and furniture refinishing</li>
    </ul>

    <address class="contact" style="font-style:normal">
      <p class="contact-title">Contact Us</p>
      <p class="contact-line">Mesquite Wallboard Company</p>
      <p class="contact-line">480-555-0173</p>
      <p class="contact-line">1480 E. Ironwood Trail</p>
      <p class="contact-line">Phoenix, AZ 8502</p>
    </address>

    <div class="brand"><span class="brand-dot"></span><span class="brand-name">Mesquite Wallboard</span></div>
    <div class="stamp-box"></div>
  </section>

</main>
</body>
</html>
```